Medical consulting firm needs polished website

I am a physician and working on setting up a smal consulting firm in New Hampshire, USA. It is called Clearpath Health Advisors, LLC and the website will be ClearpathHealthAdv.com. I was puttering around at making my own website, and it just didn't come together nicely so I've decided to leave it to the pros. The focus of the business is Advanced Care Planning, ie planning for your future medical needs. So it deals with some heavy stuff like planning for if you get sick, who should make decisions for you, end of life options etc. So it can't be too flippant or cutesy, but also can't be too dour and dark. I am hoping to convey that by thinking ahead and making some plans you can lift some of the worries off of yourself and your family - and that we can help make a scary sounding path more manageable. I want it to be made with wordpress and I have actually already bought a template ( Curova – A Bright Comprehensive Clinical & Wellness Theme ). The website needs to have general information about our services, doc profile, appointment maker, blog/url link page, and ideally web commerce application ( the template has access to woocommerce). I've posted my business card and current brochure (still tweaking them, but you get the idea). I am also partnering with lifeledgerhub.com and so have included their logo and would want connections/info about them. I have the logos etc in different formats as needed.

Target Market(s)

middle aged to older adults

Industry/Entity Type

Medical

Coding

Coded - Design and coding required

Font styles to use
Sans Serif

Requirements
Must have
• as above.
Nice to have
• Ease of reading/access for elderly viewers. woo commerce.

```html
<!DOCTYPE html>
<html lang="en">
<head>
<meta charset="utf-8">
<title>Clearpath Health Advisors</title>
<link rel="stylesheet" href="https://fonts.googleapis.com/css2?family=Open+Sans:wght@400;600;700&display=swap">
<style>
:root{
  --brand:#2a8fcf;
  --ink:#555c63;
  --ink-soft:#8a9096;
  --hero-dark:#2c3a47;
  --hero-mid:#3d5566;
  --footer-bg:#f7f7f7;
  --bar-bg:#efefef;
  --line:#e3e3e3;
  --white:#ffffff;
}
*{box-sizing:border-box;margin:0;padding:0}
html,body{width:1200px;height:1200px;overflow:hidden;background:var(--white);font-family:"Open Sans",Arial,sans-serif;color:var(--ink)}
.page{position:relative;width:1200px;height:1200px}
.abs{position:absolute}

/* hero */
.hero{left:0;top:0;width:1200px;height:430px;background:linear-gradient(180deg,#56646d 0%,#3a4d5b 50%,#2c3e4c 100%)}
.hero-photo{left:0;top:0;width:1200px;height:430px;background:linear-gradient(100deg,#6d7a82 0%,#4d5f6b 35%,#3c5566 60%,#4a6674 85%,#5b6f79 100%)}
.hero-band{left:0;top:225px;width:1200px;height:205px;background:rgba(35,52,66,.45)}
.device-photo{left:180px;top:60px;width:300px;height:370px;border-radius:30px 30px 0 0;background:linear-gradient(160deg,#f4f4f4 0%,#d9dde0 40%,#c9a99a 75%,#b98d7c 100%)}
.hero-title{left:567px;top:124px;font-size:36px;font-weight:700;color:var(--white);letter-spacing:.5px;line-height:44px}
.hero-text{left:567px;top:165px;width:520px;font-size:14px;line-height:19px;color:var(--white)}
.hero-sub{left:567px;top:211px;font-size:13px;font-weight:600;color:var(--white)}
.store-btn{top:255px;height:55px;display:flex;align-items:center;gap:14px;padding:0 22px;border-radius:2px}
.store-btn .mark{width:22px;height:22px;border-radius:50%}
.store-btn small{display:block;font-size:10px;font-weight:700;line-height:12px}
.store-btn b{display:block;font-size:15px;font-weight:700;line-height:17px;letter-spacing:.4px}
.store-dark{left:567px;width:164px;background:#3b4a58;color:var(--white)}
.store-dark .mark{background:var(--white)}
.store-light{left:741px;width:190px;background:var(--white);color:#444}
.store-light .mark{background:var(--brand)}

/* testimonials */
.reviews-title{left:0;width:1266px;top:462px;text-align:center;font-size:35px;font-weight:700;color:var(--brand);letter-spacing:.3px}
.reviews-text{left:255px;top:509px;width:756px;text-align:center;font-size:13.6px;line-height:17.6px;color:var(--ink)}
.avatar{left:597px;top:579px;width:73px;height:73px;border-radius:50%;border:1px solid #d5d5d5;padding:4px;background:var(--white)}
.avatar span{display:block;width:100%;height:100%;border-radius:50%;background:linear-gradient(180deg,#cfd8de,#e8ecef)}
.person{left:533px;width:200px;top:664px;text-align:center;font-size:13px;color:var(--ink)}
.person small{display:block;font-size:10px;margin-top:1px}
.dots{left:600px;top:711px;display:flex;gap:4px}
.dots i{width:20px;height:3px;background:#444}
.dots i:first-child{background:var(--brand)}

/* rainbow rule */
.rule{left:0;top:764px;width:1200px;height:3px;display:flex}
.rule i{flex:1}

/* footer */
.footer{left:0;top:767px;width:1200px;height:340px;background:var(--footer-bg)}
.col-title{top:806px;width:210px;font-size:19px;font-weight:700;color:var(--brand);border-bottom:1px solid var(--line);height:28px}
.col-title span{display:inline-block;border-bottom:1px solid var(--brand);height:28px}
.links{top:864px;display:grid;grid-template-columns:105px 105px;row-gap:15px;font-size:11px}
.links li{list-style:none;height:15px}
.links li::before{content:"→";margin-right:7px;color:#444}
.newsletter-text{left:435px;top:858px;width:185px;font-size:11px;line-height:18.5px}
.env{left:410px;top:864px}
.field{left:411px;width:210px;height:32px;background:var(--white);border:1px solid #eee;border-radius:2px;font-size:11px;color:var(--ink-soft);padding:8px 8px}
.subscribe{left:411px;top:993px;width:94px;height:29px;background:var(--brand);color:var(--white);font-size:10.5px;font-weight:700;border-radius:3px;text-align:center;line-height:29px;box-shadow:0 2px 0 #1f6fa3}
.tweet{left:646px;width:210px;font-size:11px;line-height:18.5px}
.tweet .dot{position:absolute;left:0;top:3px;width:12px;height:12px;border-radius:50%;background:var(--brand)}
.tweet p{margin-left:24px}
.tweet a{color:var(--brand);text-decoration:none}
.tweet small{display:block;margin-left:24px;font-size:9px;color:var(--ink-soft)}
.contact-intro{left:879px;top:858px;width:210px;font-size:11px;line-height:18.5px}
.contact{left:879px;font-size:11px;display:flex;align-items:center;gap:10px}
.contact svg{flex:none}
.social{left:880px;top:1045px;display:flex;gap:6px}
.social i{width:25px;height:24px;border:1px solid #ddd;background:var(--white);border-radius:2px}
.copy-bar{left:0;top:1107px;width:1200px;height:33px;background:var(--bar-bg);font-size:10px;text-align:center;line-height:33px;color:var(--ink);border-bottom:1px solid #ddd}
.copy-bar span{margin-left:66px}
</style>
</head>
<body>
<div class="page">

  <section class="abs hero" aria-label="App promotion">
    <div class="abs hero-photo" role="img" aria-label="Laboratory background photograph with microscope and glassware"></div>
    <div class="abs hero-band"></div>
    <div class="abs device-photo" role="img" aria-label="Hand holding a smartphone showing a lab researcher"></div>
    <h1 class="abs hero-title">CLEARPATH APP AVAILABLE</h1>
    <p class="abs hero-text">Lorem ipsum dolor sit amet, consectetuer adipiscing elit, sed diam nonummy nibh euismod tincidunt ut laoreet dolore magna aliquam erat volutpat.</p>
    <p class="abs hero-sub">AVAILABLE ON STORES</p>
    <a class="abs store-btn store-dark"><span class="mark"></span><span><small>Download From</small><b>APP HARBOR</b></span></a>
    <a class="abs store-btn store-light"><span class="mark"></span><span><small>Download From</small><b>PLAYBOOTH</b></span></a>
  </section>

  <section aria-label="Patient testimonials">
    <h2 class="abs reviews-title">WHAT OUR PATIENTS SAY ABOUT US</h2>
    <p class="abs reviews-text">Lorem ipsum dolor sit amet, consectetuer adipiscing elit, sed diam nonummy nibh euismod tincidunt ut laoreet dolore magna aliquam erat volutpat. Nam vitae felis pretium, euismod ipsum nec, placerat turpis. Aenean eu gravida arcu, et consectetur orci Quisque posuere dolor in malesuada fermentum.</p>
    <div class="abs avatar"><span role="img" aria-label="Portrait of the patient"></span></div>
    <div class="abs person">OWEN MERCER<small>HEART PATIENT</small></div>
    <div class="abs dots"><i></i><i></i><i></i></div>
  </section>

  <div class="abs rule" aria-hidden="true">
    <i style="background:#29b6e8"></i><i style="background:#9b3fa0"></i><i style="background:#ec3f7e"></i><i style="background:#f39221"></i><i style="background:#f6d216"></i><i style="background:#8cc63f"></i><i style="background:#1fa05a"></i><i style="background:#29b6e8"></i><i style="background:#9b3fa0"></i><i style="background:#ec3f7e"></i><i style="background:#f39221"></i><i style="background:#f6d216"></i><i style="background:#8cc63f"></i><i style="background:#1fa05a"></i><i style="background:#29b6e8"></i><i style="background:#9b3fa0"></i><i style="background:#ec3f7e"></i><i style="background:#f39221"></i><i style="background:#f6d216"></i><i style="background:#1fa05a"></i>
  </div>

  <footer>
    <div class="abs footer"></div>

    <h3 class="abs col-title" style="left:178px"><span>HEALVIA</span></h3>
    <ul class="abs links" style="left:178px">
      <li>Home</li><li>Doctors</li>
      <li>About US</li><li>Departments</li>
      <li>Services</li><li>Blog</li>
      <li>Why US</li><li>Medical Care</li>
      <li>Specialties</li><li>Timetable</li>
      <li>Events</li><li>Contact Us</li>
    </ul>

    <h3 class="abs col-title" style="left:411px"><span>NEWSLETTER</span></h3>
    <svg class="abs env" width="20" height="18" viewBox="0 0 20 18" aria-hidden="true"><path d="M1 7 L17 1 L14 16 Z" fill="#333"/><path d="M1 7 L14 16" stroke="#f7f7f7" stroke-width="1.2"/></svg>
    <p class="abs newsletter-text">Sign up with your name and email to get updates fresh updates.</p>
    <div class="abs field" style="top:914px">Your Name</div>
    <div class="abs field" style="top:952px">Email Address</div>
    <div class="abs subscribe">SUBSCRIBE</div>

    <h3 class="abs col-title" style="left:646px"><span>LATEST TWEETS</span></h3>
    <div class="abs tweet" style="top:864px"><span class="dot"></span><p><a>@Dana Whitcomb</a>, MD Please kindly use our Support Forum: <a>clearpathhealthadv.com</a></p><small>about a month ago</small></div>
    <div class="abs tweet" style="top:954px"><span class="dot"></span><p><a>@Dana Whitcomb</a>, MD Please kindly use our Support Forum: <a>clearpathhealthadv.com</a></p><small>about a month ago</small></div>

    <h3 class="abs col-title" style="left:879px"><span>GET IN TOUCH</span></h3>
    <p class="abs contact-intro">Clearpath, Medical Services, Because Someday is Soon</p>
    <div class="abs contact" style="top:915px"><svg width="20" height="15" viewBox="0 0 20 15" aria-hidden="true"><rect x="0" y="0" width="20" height="15" rx="1" fill="#555"/><path d="M1 1 L10 8 L19 1" stroke="#f7f7f7" stroke-width="1.5" fill="none"/></svg>info@clearpathhealthadv.com</div>
    <div class="abs contact" style="top:943px"><svg width="18" height="18" viewBox="0 0 18 18" aria-hidden="true"><circle cx="9" cy="9" r="8.5" fill="#555"/><path d="M9 .5 V17.5 M.5 9 H17.5" stroke="#f7f7f7" stroke-width="1.2"/><ellipse cx="9" cy="9" rx="4" ry="8.5" stroke="#f7f7f7" stroke-width="1.2" fill="none"/></svg>www.ClearpathHealthAdv.com</div>
    <div class="abs contact" style="top:973px"><svg width="17" height="17" viewBox="0 0 17 17" aria-hidden="true"><path d="M3 1 L6 1 L7 5 L5 6.5 Q7 10.5 10.5 12 L12 10 L16 11 L16 14 Q15 16 12.5 16 Q2 13 1 3.5 Q1 1 3 1 Z" fill="#555"/></svg>(+1) 603 555 0142</div>
    <div class="abs contact" style="top:1010px;left:907px">(+1) 603 555 0187</div>
    <div class="abs social" aria-label="Social links"><i></i><i></i><i></i><i></i><i></i><i></i></div>

    <div class="abs copy-bar"><span>Copyright © 2016 CLEARPATH. All right reserved.</span></div>
  </footer>
</div>
</body>
</html>
```